Simple and Clean business card design

We would like the design to be simple clean and to incorporate our colors.

We are open to your design and talent, we have the dots in our logo as we think of it as data points and we connect data points for people.

We are open to see the great creative and clean design you bring to the table

Contact Information for Business Card

please include: name, position, email, phone and website

Font styles to use
Sans Serif

Requirements
Must have
• my colors incorporated, simplicity
Nice to have
• lots of white space, simplicity
Should not have
• complexicity/ complex art

```html
<!DOCTYPE html>
<html lang="en">
<head>
<meta charset="utf-8">
<title>Nodera – Business Card</title>
<link rel="stylesheet" href="https://fonts.googleapis.com/css2?family=Poppins:wght@400;600;700&display=swap">
<style>
  :root {
    --page: #e9e6e1;
    --card: #f7f7f7;
    --ink: #111111;
    --blue: #4285f4;
    --yellow: #f7cd3c;
    --green: #4fae63;
    --red: #f26b5b;
    --mail-green: #5cb66f;
    --phone-yellow: #f6d35a;
    --web-salmon: #f28b80;
  }
  * { margin: 0; padding: 0; box-sizing: border-box; }
  html, body {
    width: 1200px;
    height: 1200px;
    overflow: hidden;
    background: var(--page);
    font-family: "Poppins", sans-serif;
    color: var(--ink);
  }
  .canvas {
    position: relative;
    width: 1200px;
    height: 1200px;
  }
  .card {
    position: absolute;
    left: 150px;
    width: 900px;
    height: 514px;
    background: var(--card);
    overflow: hidden;
    box-shadow: 0 10px 30px rgba(0,0,0,0.12);
  }
  .card--back { top: 60px; }
  .card--front { top: 626px; }

  /* Back side */
  .brand {
    position: absolute;
    left: 96px;
    top: 120px;
    display: flex;
    align-items: center;
    gap: 14px;
  }
  .brand__dot {
    width: 22px;
    height: 22px;
    border-radius: 50%;
    background: var(--blue);
  }
  .brand__name {
    font-weight: 600;
    font-size: 52px;
    letter-spacing: 1px;
    color: var(--ink);
  }
  .network-art {
    position: absolute;
    right: 0;
    bottom: 0;
    width: 420px;
    height: 420px;
    clip-path: polygon(40% 8%, 62% 0, 100% 12%, 100% 100%, 0 100%, 20% 62%, 34% 40%);
    background: radial-gradient(circle at 60% 50%, rgba(66,133,244,0.16), rgba(247,205,60,0.12) 45%, rgba(242,107,91,0.06) 75%, rgba(247,247,247,0) 100%);
  }

  /* Front side */
  .identity {
    position: absolute;
    left: 120px;
    top: 96px;
  }
  .identity__name {
    font-weight: 700;
    font-size: 62px;
    line-height: 1;
  }
  .identity__position {
    font-weight: 400;
    font-size: 26px;
    letter-spacing: 19px;
    margin-top: 2px;
  }
  .contacts {
    position: absolute;
    left: 120px;
    top: 222px;
    list-style: none;
  }
  .contacts__item {
    display: flex;
    align-items: center;
    gap: 16px;
    font-size: 24px;
    line-height: 1;
    margin-bottom: 12px;
  }
  .contacts__icon {
    width: 28px;
    height: 28px;
    flex: none;
  }
  .corner-art {
    position: absolute;
    right: 0;
    bottom: 0;
    width: 360px;
    height: 280px;
    background: radial-gradient(ellipse at 100% 100%, rgba(242,107,91,0.30), rgba(247,205,60,0.20) 40%, rgba(79,174,99,0.12) 65%, rgba(247,247,247,0) 90%);
  }
</style>
</head>
<body>
<main class="canvas">

  <section class="card card--back" aria-label="Card back">
    <div class="brand">
      <span class="brand__dot"></span>
      <span class="brand__name">Nodera</span>
    </div>
    <div class="network-art" role="img" aria-label="Light pattern of coloured data points joined by thin grey lines"></div>
  </section>

  <section class="card card--front" aria-label="Card front">
    <div class="identity">
      <h1 class="identity__name">Your Name</h1>
      <p class="identity__position">Posisition</p>
    </div>

    <ul class="contacts">
      <li class="contacts__item">
        <svg class="contacts__icon" viewBox="0 0 28 28" aria-hidden="true">
          <circle cx="14" cy="14" r="14" fill="var(--mail-green)"/>
          <rect x="7" y="9" width="14" height="10" fill="none" stroke="#fff" stroke-width="1.6"/>
          <path d="M7 9 L14 15 L21 9" fill="none" stroke="#fff" stroke-width="1.6"/>
        </svg>
        <span>Yourmail@mail.com</span>
      </li>
      <li class="contacts__item">
        <svg class="contacts__icon" viewBox="0 0 28 28" aria-hidden="true">
          <circle cx="14" cy="14" r="14" fill="var(--phone-yellow)"/>
          <path d="M10 8 L12.5 8 L13.5 11 L12 12.3 Q13.5 15.5 15.7 16 L17 14.5 L20 15.5 L20 18 Q19 20 16.5 19.5 Q10 17.5 8.5 11 Q8.2 8.8 10 8 Z" fill="#fff"/>
        </svg>
        <span>1234567890</span>
      </li>
      <li class="contacts__item">
        <svg class="contacts__icon" viewBox="0 0 28 28" aria-hidden="true">
          <circle cx="14" cy="14" r="14" fill="var(--web-salmon)"/>
          <circle cx="14" cy="14" r="7" fill="none" stroke="#fff" stroke-width="1.5"/>
          <ellipse cx="14" cy="14" rx="3" ry="7" fill="none" stroke="#fff" stroke-width="1.3"/>
          <line x1="7" y1="14" x2="21" y2="14" stroke="#fff" stroke-width="1.3"/>
        </svg>
        <span>www.yourwebsite.com</span>
      </li>
    </ul>

    <div class="corner-art" role="img" aria-label="Decorative group of overlapping coloured circles in blue, yellow, green and red"></div>
  </section>

</main>
</body>
</html>
```